Stationery and business card design
TradeNimbus
Stationery and business card design -
Creative Brief
Corporate
Marcella Quenby, PHR, PMP
Project Manager
4172 Birchwell Rd NE #20591 Oakhollow, MI 48273
mquenby@tradenimbus.example
http://www.tradenimbus.example
stationary will be for corporate entity no specific individual

```html
<!DOCTYPE html>
<html lang="en">
<head>
<meta charset="utf-8">
<title>TradeNimbus Stationery</title>
<link href="https://fonts.googleapis.com/css2?family=Open+Sans:wght@400;600;700&display=swap" rel="stylesheet">
<style>
  :root {
    --blue: #2f74c0;
    --blue-dark: #1f5ea6;
    --orange: #f39a1d;
    --paper: #ffffff;
    --ink: #3a4a5c;
    --muted: #6d7a88;
    --bg: #e9e6e1;
  }
  * { margin: 0; padding: 0; box-sizing: border-box; }
  html, body { width: 1200px; height: 869px; overflow: hidden; }
  body { background: var(--bg); font-family: "Open Sans", Arial, sans-serif; color: var(--ink); position: relative; }

  .sheet { position: absolute; background: var(--paper); box-shadow: 0 2px 8px rgba(0,0,0,.18); overflow: hidden; }
  .wave { position: absolute; left: 0; top: 0; width: 100%; display: block; }

  .brand { position: absolute; display: flex; align-items: center; gap: 6px; }
  .brand-dot { border-radius: 50%; background: var(--blue); flex: none; }
  .brand-name { font-weight: 600; color: var(--blue-dark); letter-spacing: -.3px; line-height: 1; white-space: nowrap; }
  .tagline { position: absolute; color: var(--orange); line-height: 1; white-space: nowrap; }

  .contact { position: absolute; color: var(--muted); line-height: 1.45; white-space: nowrap; }
  .contact .label { color: var(--orange); }
  .contact .link { color: var(--blue); }

  /* letterhead */
  .letterhead { left: 48px; top: 91px; width: 499px; height: 701px; }
  .letterhead .brand { left: 20px; top: 80px; }
  .letterhead .brand-dot { width: 16px; height: 16px; }
  .letterhead .brand-name { font-size: 32px; }
  .letterhead .tagline { left: 42px; top: 118px; font-size: 13px; }
  .letterhead .contact { left: 22px; bottom: 22px; font-size: 8.5px; }

  /* business card */
  .card { left: 667px; top: 134px; width: 221px; height: 137px; }
  .card .brand { left: 10px; top: 38px; }
  .card .brand-dot { width: 8px; height: 8px; }
  .card .brand-name { font-size: 15px; }
  .card .tagline { left: 24px; top: 57px; font-size: 6.5px; }
  .card .contact { left: 12px; top: 80px; font-size: 5px; }
  .card .person { position: absolute; right: 12px; top: 95px; text-align: right; white-space: nowrap; }
  .card .person-name { font-size: 7px; font-weight: 600; color: var(--blue-dark); }
  .card .person-role { font-size: 5.5px; color: var(--orange); }

  /* envelope back */
  .envelope-back { left: 518px; top: 331px; width: 629px; height: 192px; }
  .envelope-back .flap-mark { position: absolute; left: 302px; top: 42px; width: 24px; height: 24px; border-radius: 50%; background: var(--paper); }

  /* envelope front */
  .envelope-front { left: 562px; top: 427px; width: 585px; height: 269px; }
  .envelope-front .brand { left: 22px; top: 64px; }
  .envelope-front .brand-dot { width: 12px; height: 12px; }
  .envelope-front .brand-name { font-size: 24px; }
  .envelope-front .tagline { left: 40px; top: 92px; font-size: 10px; }
  .envelope-front .contact { left: 22px; bottom: 18px; font-size: 7.5px; }
</style>
</head>
<body>

<section class="sheet letterhead">
  <svg class="wave" viewBox="0 0 500 100" height="100" preserveAspectRatio="none" aria-hidden="true">
    <path d="M0 0 H500 V34 C380 8 200 40 0 58 Z" fill="var(--blue)"/>
    <path d="M0 58 C200 40 380 8 500 34 V40 C380 16 200 48 0 66 Z" fill="var(--orange)"/>
  </svg>
  <div class="brand"><span class="brand-dot"></span><span class="brand-name">TradeNimbus</span></div>
  <div class="tagline">Supplier Sourcing Streamlined</div>
  <div class="contact">
    4172 Birchwell Rd NE #20591<br>Oakhollow, MI 48273<br>
    <span class="label">Toll Free:</span> +1 800-555-0142<br>
    <span class="label">E-mail:</span> mquenby@tradenimbus.example<br>
    <span class="link">http://www.tradenimbus.example</span>
  </div>
</section>

<section class="sheet card">
  <svg class="wave" viewBox="0 0 220 40" height="40" preserveAspectRatio="none" aria-hidden="true">
    <path d="M0 0 H220 V14 C160 4 90 18 0 26 Z" fill="var(--blue)"/>
    <path d="M0 26 C90 18 160 4 220 14 V17 C160 8 90 22 0 30 Z" fill="var(--orange)"/>
  </svg>
  <div class="brand"><span class="brand-dot"></span><span class="brand-name">TradeNimbus</span></div>
  <div class="tagline">Supplier Sourcing Streamlined</div>
  <div class="contact">
    4172 Birchwell Rd NE #20591<br>Oakhollow, MI 48273<br>
    <span class="label">Toll Free:</span> +1 800-555-0142<br>
    <span class="label">Fax:</span> +1 800-555-0199<br>
    mquenby@tradenimbus.example<br>
    <span class="link">http://www.tradenimbus.example</span>
  </div>
  <div class="person">
    <div class="person-name">Marcella Quenby, PHR, PMP</div>
    <div class="person-role">Project Manager</div>
  </div>
</section>

<section class="sheet envelope-back">
  <svg class="wave" viewBox="0 0 629 110" height="110" preserveAspectRatio="none" aria-hidden="true">
    <path d="M0 0 H629 V24 C500 34 380 60 314 100 C250 60 130 34 0 24 Z" fill="var(--blue)"/>
  </svg>
  <span class="flap-mark"></span>
</section>

<section class="sheet envelope-front">
  <svg class="wave" viewBox="0 0 585 60" height="60" preserveAspectRatio="none" aria-hidden="true">
    <path d="M0 0 H585 V20 C440 6 240 26 0 40 Z" fill="var(--blue)"/>
    <path d="M0 40 C240 26 440 6 585 20 V25 C440 11 240 31 0 46 Z" fill="var(--orange)"/>
  </svg>
  <div class="brand"><span class="brand-dot"></span><span class="brand-name">TradeNimbus</span></div>
  <div class="tagline">Supplier Sourcing Streamlined</div>
  <div class="contact">
    4172 Birchwell Rd NE #20591<br>Oakhollow, MI 48273<br>
    <span class="label">Toll Free:</span> +1 800-555-0142<br>
    <span class="label">E-mail:</span> mquenby@tradenimbus.example<br>
    <span class="link">http://www.tradenimbus.example</span>
  </div>
</section>

</body>
</html>
```